Package Storage Service

Ideas...

Business Name... "TUCK IT AT BRAMWOOD":
Store it,
Don’t Ship it;
4-LESS
Convenience, Quality, Service

Easy as ABC…
A. Contact Us 064-293-5527
B. We deliver
C. We pick-up & Store

LESS, is the new MORE

Box Size* (Approx) Weight Limit Price per Month
41 cm X 34 cm X 26 cm 10 Kilos 12 CHFs/per month
48 cm X 43 cm X 35 cm 25 Kilos 25 CHFs/per month

* Larger sizes and prices available upon request.

Contact: Tom /064-293-5527

These are only ideas for a small package storage service for local college students. The storage times are usually for 1 - 3 months.
I need a catchy, creative, colorful design for a new business.

This flyer will need to be printable in color. A-4 size or 8 1/2 " X 11".

Target Market(s)

Hotel Management students leaving their program for vacations for short terms. They return after vacation or after practical work experiences 4 study.

Industry/Entity Type

College

Requirements
Must have
• Prices, box sizes, catchy format.

Idea will forward to their address should they not return to the school; for a postage fee + 15.00 CHFs.

Contact information for the PICKUP and DELIVERY Service... see above.

Include a PICKUP AND DELIVERY Option in the flyer.
Nice to have
• Colorful boxes with a creative idea for someone to choose spending a little each month rather than a lot at one time. 25 CHFs rather than 125 CHFs.
Should not have
• Not too wordy.

```html
<!DOCTYPE html>
<html lang="en">
<head>
<meta charset="utf-8">
<title>Tuck It At Bramwood – Package Storage Flyer</title>
<link rel="stylesheet" href="https://fonts.googleapis.com/css2?family=Suez+One&family=Arimo:wght@400;700&display=swap">
<style>
  :root {
    --page-bg: #e9e6e1;
    --paper: #fbfaf7;
    --green: #74e46f;
    --green-line: #c9f6c6;
    --orange: #e8913a;
    --band-orange: #e29a5c;
    --pink: #e3147a;
    --icon-grey: #6a6f74;
    --ink-dark: #2c2c2c;
    --white: #ffffff;
  }
  * { box-sizing: border-box; margin: 0; padding: 0; }
  html, body { width: 1200px; height: 900px; overflow: hidden; }
  body { background: var(--page-bg); position: relative; font-family: "Suez One", Georgia, serif; }

  .flyer {
    position: absolute; left: 305px; top: 27px; width: 590px; height: 845px;
    background: var(--paper); overflow: hidden;
    box-shadow: 0 2px 10px rgba(0,0,0,.18);
  }

  .hero-photo {
    position: absolute; left: 0; top: 0; width: 100%; height: 455px;
    background:
      radial-gradient(ellipse at 45% 40%, #d9c3a8 0%, rgba(217,195,168,0) 55%),
      linear-gradient(180deg, #efe7dd 0%, #d8bc98 35%, #cfae86 60%, #ede4da 85%, var(--paper) 100%);
  }

  .headline { position: absolute; left: 20px; top: 12px; font-size: 30px; line-height: 32px; font-weight: 400; color: var(--white); }
  .headline span {
    display: inline-block; background: var(--green); padding: 0 10px; border-radius: 12px;
  }

  .tagline {
    position: absolute; left: 26px; top: 296px; font-size: 28px; line-height: 30px; color: var(--orange);
    text-shadow: 0 0 3px #fff, 0 0 3px #fff, 2px 2px 0 #fff, -2px -2px 0 #fff, 2px -2px 0 #fff, -2px 2px 0 #fff;
  }

  .steps-title {
    position: absolute; left: 18px; top: 451px; font-family: "Arimo", Arial, sans-serif;
    font-size: 30px; line-height: 34px; font-weight: 400; color: var(--pink);
  }

  .step-icon { position: absolute; fill: var(--icon-grey); }
  .icon-phone { left: 90px; top: 495px; width: 48px; height: 56px; }
  .icon-boxes { left: 217px; top: 510px; width: 163px; height: 62px; }
  .icon-truck { left: 447px; top: 510px; width: 84px; height: 64px; }

  .phone-number {
    position: absolute; left: 25px; top: 554px; width: 180px; text-align: center;
    font-size: 19px; line-height: 22px; letter-spacing: 1.5px; color: var(--ink-dark);
  }

  .step-bar { position: absolute; left: 17px; top: 581px; width: 559px; height: 28px; }
  .step-label { position: absolute; top: 581px; height: 28px; color: var(--white); display: flex; align-items: center; font-size: 19px; letter-spacing: 1px; }
  .step-label.a { left: 28px; }
  .step-label.b { left: 222px; }
  .step-label.c { left: 394px; }
  .step-label.c small { font-size: 11px; line-height: 11px; text-align: center; margin-left: 14px; letter-spacing: 0; }

  .motto-rule { position: absolute; left: 0; width: 100%; height: 2px; background: var(--pink); }
  .motto-rule.top { top: 626px; }
  .motto-rule.bottom { top: 667px; }
  .motto {
    position: absolute; left: 0; top: 629px; width: 100%; text-align: center;
    font-size: 29px; line-height: 36px; font-style: italic; color: var(--pink);
  }

  .price-table {
    position: absolute; left: 17px; top: 683px; width: 559px; border-collapse: separate; border-spacing: 0;
    background: var(--green); border-radius: 9px; overflow: hidden; color: var(--white);
  }
  .price-table th { font-weight: 400; font-size: 17px; height: 29px; letter-spacing: .5px; }
  .price-table td { font-size: 15px; height: 27px; text-align: center; letter-spacing: .5px; border-top: 1px solid var(--green-line); }
  .price-table td + td { border-left: 1px solid var(--green-line); }

  .contact-band {
    position: absolute; left: 0; top: 778px; width: 100%; height: 67px; background: var(--band-orange);
    color: var(--white); text-align: center;
  }
  .contact-band .note { font-size: 18px; line-height: 22px; margin-top: 6px; letter-spacing: .3px; }
  .contact-band .contact { font-size: 24px; line-height: 30px; margin-top: 2px; letter-spacing: .5px; }
</style>
</head>
<body>
  <main class="flyer" aria-label="TUCK IT AT BRAMWOOD package storage flyer">
    <div class="hero-photo" role="img" aria-label="Photo of a stressed young woman among cardboard boxes while a young man carries a large moving box"></div>

    <h1 class="headline"><span>Don't know what to do with</span><br><span>your stuff.......??</span></h1>

    <p class="tagline">Store it,<br>Don't Ship it;<br>4-LESS<br>Convenience, Quality, Service</p>

    <h2 class="steps-title">Easy as ABC…</h2>

    <svg class="step-icon icon-phone" viewBox="0 0 50 58" aria-hidden="true">
      <path d="M8 2 L18 2 L20 14 L13 19 C16 30 22 38 30 44 L36 38 L47 42 L46 52 C44 56 40 57 35 56 C17 50 5 33 2 14 C2 8 4 3 8 2 Z"/>
    </svg>

    <svg class="step-icon icon-boxes" viewBox="0 0 163 64" aria-hidden="true">
      <path d="M0 14 L8 2 L22 14 L30 2 L44 14 L52 2 L66 14 L66 64 L0 64 Z"/>
      <path d="M70 26 L77 18 L86 26 L93 18 L102 26 L108 18 L116 26 L116 64 L70 64 Z"/>
      <path d="M120 36 L126 30 L133 36 L139 30 L146 36 L152 30 L160 36 L160 64 L120 64 Z"/>
      <g fill="#fbfaf7"><rect x="30" y="44" width="6" height="4"/><rect x="90" y="50" width="5" height="3"/><rect x="137" y="54" width="4" height="3"/></g>
    </svg>

    <svg class="step-icon icon-truck" viewBox="0 0 86 68" aria-hidden="true">
      <rect x="0" y="0" width="46" height="42" rx="3"/>
      <path d="M23 8 L33 19 L27 19 L27 30 L19 30 L19 19 L13 19 Z" fill="#fbfaf7"/>
      <rect x="0" y="44" width="50" height="8"/>
      <path d="M52 14 L72 14 L84 30 L84 52 L52 52 Z"/>
      <path d="M57 19 L70 19 L78 30 L57 30 Z" fill="#fbfaf7"/>
      <circle cx="16" cy="57" r="10"/><circle cx="70" cy="57" r="10"/>
      <circle cx="16" cy="57" r="4" fill="#fbfaf7"/><circle cx="70" cy="57" r="4" fill="#fbfaf7"/>
    </svg>

    <p class="phone-number">064-293-5527</p>

    <svg class="step-bar" viewBox="0 0 559 28" aria-hidden="true">
      <path d="M8 0 L187 0 L195 14 L187 28 L8 28 Q0 28 0 20 L0 8 Q0 0 8 0 Z" fill="var(--green)"/>
      <path d="M192 0 L365 0 L373 14 L365 28 L192 28 L200 14 Z" fill="var(--green)"/>
      <path d="M370 0 L551 0 Q559 0 559 8 L559 20 Q559 28 551 28 L370 28 L378 14 Z" fill="var(--green)"/>
    </svg>
    <div class="step-label a">A. Contact Us</div>
    <div class="step-label b">B. We deliver</div>
    <div class="step-label c">C. <small>We pick-up<br>&amp; Store</small></div>

    <div class="motto-rule top"></div>
    <p class="motto">LESS, is the new MORE</p>
    <div class="motto-rule bottom"></div>

    <table class="price-table">
      <thead>
        <tr><th>Box Size* (Approx)</th><th>Weight Limit</th><th>Price per Month</th></tr>
      </thead>
      <tbody>
        <tr><td>41 cm X 34 cm X 26 cm</td><td>10 Kilos</td><td>12 CHFs/per month</td></tr>
        <tr><td>48 cm X 43 cm X 35 cm</td><td>25 Kilos</td><td>25 CHFs/per month</td></tr>
      </tbody>
    </table>

    <footer class="contact-band">
      <p class="note">*Larger sizes and prices available upon request.</p>
      <p class="contact">Contact: Tom/064-293-5527</p>
    </footer>
  </main>
</body>
</html>
```